K7 seamless

We are a glazing company specializing in frameless glass .
I would like the business cards in black with the logo taking up the most part of the front added with " frameless glass specialist's " below it.
On the back side I would like a list of what we do :
• shower screens
• glass balustrade / pool fencing
• mirrors
•office partitions
• sky lights
•shop fronts
•splash backs
Also include this information :
📧 - corbin@k7seamless.com
📞Corbin - 0418276594
📞 Milo - 0427 613 508
Updates
To all designs already posted can you include on the back of the card in the services part -
•splash backs
Target Market(s)
High end builders
Industry/Entity Type
Glazing
Contact Information for Business Card
On the back side I would like a list of what we do : • shower screens • glass balustrade / pool fencing • mirrors •office partitions • sky lights •shop fronts Also include this information : 📧 - corbin@k7seamless.com 📞Corbin - 0418276594 📞 Milo - 0427 613 508
Colors
Designer to choose colors to be used in the design.
Look and feel
Each slider illustrates characteristics of the customer's brand and the style your logo design should communicate.

```html
<!DOCTYPE html>
<html lang="en">
<head>
<meta charset="utf-8">
<title>K7 seamless — business card</title>
<link rel="stylesheet" href="https://fonts.googleapis.com/css2?family=Montserrat:wght@400;500;600;700&display=swap">
<style>
  :root {
    --backdrop: #8a6f52;
    --card: #000000;
    --teal: #3cbfa6;
    --teal-deep: #1b9aa0;
    --white: #ffffff;
    --text-light: #f2f2f2;
    --grey-mark: #8c8c8c;
    --rule-grey: #9a9a9a;
  }
  * { box-sizing: border-box; margin: 0; padding: 0; }
  html, body { width: 900px; height: 1200px; overflow: hidden; }
  body {
    background: var(--backdrop);
    font-family: "Montserrat", Arial, sans-serif;
    position: relative;
  }
  .card {
    position: absolute;
    left: 68px;
    width: 758px;
    height: 442px;
    background: var(--card);
    border-radius: 28px;
    overflow: hidden;
  }
  .card--front { top: 132px; }
  .card--back { top: 636px; height: 444px; }

  .brand {
    position: absolute;
    width: 300px;
    text-align: center;
  }
  .card--front .brand { left: 66px; top: 182px; color: var(--teal); }
  .card--back .brand { left: 56px; top: 182px; color: var(--grey-mark); }
  .brand__name {
    font-size: 40px;
    font-weight: 600;
    white-space: nowrap;
    line-height: 1.1;
  }
  .brand__tagline {
    font-size: 14px;
    font-weight: 500;
    letter-spacing: 1px;
    margin-top: 8px;
    white-space: nowrap;
  }

  .divider {
    position: absolute;
    width: 2px;
  }
  .card--front .divider { left: 383px; top: 104px; height: 222px; background: var(--teal-deep); }
  .card--back .divider { left: 386px; top: 104px; height: 270px; background: var(--rule-grey); }

  .contact { position: absolute; left: 430px; top: 100px; color: var(--text-light); }
  .contact__name { font-size: 25px; font-weight: 700; color: var(--teal); line-height: 1.1; }
  .contact__role { font-size: 16px; margin-top: 8px; }
  .contact__address { font-size: 16px; line-height: 20px; margin-top: 25px; }
  .contact__list { list-style: none; margin-top: 14px; }
  .contact__list li {
    display: flex; align-items: center;
    font-size: 16px; height: 25px;
  }
  .contact__list svg { width: 16px; height: 16px; margin-right: 14px; fill: var(--teal-deep); flex: none; }
  .accent { color: var(--teal); }
  .accent--bold { color: var(--teal); font-weight: 700; }

  .footer-band { position: absolute; left: 0; bottom: 0; width: 758px; height: 40px; }
  .footer-url {
    position: absolute; right: 92px; bottom: 8px;
    font-size: 15px; color: #111; font-weight: 500;
  }

  .services { position: absolute; left: 438px; top: 96px; color: var(--text-light); }
  .services__title {
    font-size: 28px; font-weight: 400; color: var(--teal-deep);
    padding: 0 4px 6px 3px; border-bottom: 2px solid var(--text-light);
    display: inline-block; width: 182px;
  }
  .services__list { list-style: none; margin-top: 20px; }
  .services__list li {
    font-size: 17px; height: 31px; display: flex; align-items: center;
  }
  .services__list li::before {
    content: ""; width: 9px; height: 9px; border-radius: 50%;
    background: var(--teal); margin: 0 10px 0 2px;
  }
</style>
</head>
<body>

<section class="card card--front">
  <div class="brand">
    <div class="brand__name">K7 seamless</div>
    <div class="brand__tagline">frameless glass specialists</div>
  </div>
  <div class="divider"></div>

  <div class="contact">
    <div class="contact__name">Tobias Renard</div>
    <div class="contact__role">Owner</div>
    <div class="contact__address">418 Harlow Lane, #112<br>Brookfield, OH 44019</div>
    <ul class="contact__list">
      <li>
        <svg viewBox="0 0 16 16" aria-hidden="true"><path d="M1 5c0-2 3-3 7-3s7 1 7 3v1.5h-3.5V5h-7v1.5H1zM3 8l2-2h6l2 2v5H3zm5 1a2 2 0 100 4 2 2 0 000-4z"/></svg>
        0418276594&nbsp;<span class="accent">(Corbin)</span>
      </li>
      <li>
        <svg viewBox="0 0 16 16" aria-hidden="true"><path d="M4.5 0h7a1 1 0 011 1v14a1 1 0 01-1 1h-7a1 1 0 01-1-1V1a1 1 0 011-1zm.5 2v10h6V2zm3 11a1 1 0 100 2 1 1 0 000-2z"/></svg>
        0427 613 508&nbsp;<span class="accent">(Milo)</span>
      </li>
      <li>
        <svg viewBox="0 0 16 16" aria-hidden="true"><path d="M1 4h14v1.2L8 9 1 5.2zm0 2.6L8 10.4l7-3.8V12H1z"/></svg>
        corbin@<span class="accent--bold">k7seamless</span>.com
      </li>
      <li>
        <svg viewBox="0 0 16 16" aria-hidden="true"><path d="M8 1a7 7 0 100 14A7 7 0 008 1zm-1 2.5l1 1.5-1.5 1 1 2-2 1-1-2.5L3 5.5A5.5 5.5 0 017 3.5zm3.5 1.2A5.5 5.5 0 0113 10l-2 .5-1-2 1.5-1.5z"/></svg>
        www.<span class="accent--bold">k7seamless</span>.com
      </li>
    </ul>
  </div>

  <svg class="footer-band" viewBox="0 0 758 40" aria-hidden="true">
    <polygon points="0,22 392,22 386,40 0,40" fill="var(--teal)"/>
    <polygon points="416,4 758,4 758,40 388,40" fill="var(--white)"/>
  </svg>
  <div class="footer-url">www.k7seamless.com</div>
</section>

<section class="card card--back">
  <div class="brand">
    <div class="brand__name">K7 seamless</div>
    <div class="brand__tagline">frameless glass specialists</div>
  </div>
  <div class="divider"></div>

  <div class="services">
    <h2 class="services__title">Our services</h2>
    <ul class="services__list">
      <li>shower screens</li>
      <li>glass balustrade / pool fencing</li>
      <li>mirrors</li>
      <li>office partitions</li>
      <li>sky lights</li>
      <li>shop fronts</li>
      <li>splash backs</li>
    </ul>
  </div>
</section>

</body>
</html>
```